Life Coaching and Career Coaching company needs new website with bold, modern, videos

We need a whole new website that is heavy on video. We are a small company who sells personal wellbeing services like career coaching, life coaching, and group coaching programs. The programs all help people design a better life.
FULL BRIEF ATTACHED and STYLE GUIDE
Also, look at https://www.brightfennel.com/coaching and galdrove.com and https://www.marnwick.life/ for a small amount of inspiration.

Industry/Entity Type

personal well-being/life coaching/career coaching

Number of Pages Required

3 page

Other font styles liked:
• fonts are in the brief

Requirements
Must have
• read the brief please - it's all in there. (things like the look, feel, how it will have lots of video, etc,)
Nice to have
• something really different looking and breakthrough. visually stunning. very trustworthy. Please read the brief, its all in there.
Should not have
• should not look like other life coaching websites. must have video!

```html
<!DOCTYPE html>
<html lang="en">
<head>
<meta charset="utf-8">
<title>Lumen Path — Transform Your Life By Design</title>
<link href="https://fonts.googleapis.com/css2?family=Righteous&family=Jost:wght@400;500;600&display=swap" rel="stylesheet">
<style>
:root{
  --coral:#ef6461;
  --teal:#0c5b5f;
  --ink:#121212;
  --body:#3a3a3a;
  --grey:#6f6f73;
  --band:#ebe7ec;
  --white:#ffffff;
}
*{box-sizing:border-box;margin:0;padding:0}
html,body{width:1200px;height:3010px;overflow:hidden}
body{position:relative;background:var(--white);font-family:'Jost',sans-serif;color:var(--ink)}
.abs{position:absolute}
.display{font-family:'Righteous',sans-serif;font-weight:400}
.accent{color:var(--teal)}
.btn{position:absolute;display:flex;align-items:center;justify-content:center;background:var(--coral);color:var(--white);font-size:13px;font-weight:500;height:35px}
.photo{position:absolute}
.play{position:absolute;width:60px;height:60px}

/* header */
.site-header{position:absolute;left:0;top:0;width:1200px;height:70px;background:var(--white)}
.brand{position:absolute;left:146px;top:18px;font-size:27px;font-weight:400;color:var(--grey);letter-spacing:1px}

/* hero */
.hero{position:absolute;left:0;top:70px;width:1200px;height:473px;background:linear-gradient(90deg,#5d5a55 0%,#8d8c88 35%,#c9d0d4 60%,#dfe4e6 80%,#b9b4ac 100%)}
.hero-title{position:absolute;left:141px;font-size:48px;line-height:70px;color:var(--white)}
.hero-sub{position:absolute;left:141px;font-size:17.5px;font-weight:500;color:var(--white)}

/* shared section copy */
.copy p{font-size:14.2px;line-height:22.7px;color:var(--body)}
.frame-red{position:absolute;border-top:1.5px solid var(--coral);border-left:1.5px solid var(--coral);border-right:1.5px solid var(--coral)}
.frame-teal{position:absolute;border:1.5px solid var(--teal)}
.section-title{position:absolute;font-size:31px}

/* programs */
.card{position:absolute;top:1114px;width:294px}
.card .photo{position:static;width:294px;height:222px}
.card h3{position:absolute;top:240px;left:0;font-size:16px;font-weight:600}
.card p{position:absolute;top:272px;left:0;font-size:14.2px;line-height:22.7px;color:var(--body)}

/* testimonial */
.testimonial{position:absolute;left:0;top:1614px;width:1200px;height:410px;background:var(--band)}

/* footer */
.site-footer{position:absolute;left:0;top:2635px;width:1200px;height:375px;background:radial-gradient(ellipse at 50% 40%,#4a403a 0%,#2e2724 60%,#1f1b19 100%)}
.footer-brand{position:absolute;left:479px;top:56px;width:242px;height:67px;background:var(--white);display:flex;align-items:center;justify-content:center;font-size:32px;color:var(--grey);letter-spacing:1px}
.contact{position:absolute;top:224px;display:flex;gap:8px;font-size:16.5px;color:var(--white);line-height:24px}
.rule{position:absolute;left:141px;top:315px;width:918px;height:1px;background:rgba(255,255,255,.25)}
.legal{position:absolute;top:336px;font-size:14.5px;color:var(--white)}
</style>
</head>
<body>

<header class="site-header">
  <div class="brand">LUMEN PATH</div>
  <div class="btn" style="left:938px;top:18px;width:121px">Sign Up Now</div>
</header>

<section class="hero" role="img" aria-label="Photo of a smiling coach presenting at a whiteboard to a seated group">
  <h1 class="hero-title display" style="top:143px">Transform Your<br>Life By Design</h1>
  <p class="hero-sub" style="top:297px">Expert Coaches for All Backgrounds</p>
  <div class="btn" style="left:141px;top:348px;width:176px">Explore Our Programs</div>
</section>

<!-- welcome -->
<div class="frame-red" style="left:141px;top:629px;width:278px;height:237px"></div>
<div class="photo" role="img" aria-label="Photo of a coach leading a workshop for a small seated group in a bright office" style="left:159px;top:646px;width:377px;height:286px;background:linear-gradient(135deg,#e7e9ea,#b9bcbc 55%,#6d6a66)"></div>
<div class="frame-teal" style="left:421px;top:830px;width:131px;height:119px"></div>
<div class="abs" style="left:622px;top:645px;font-size:16px;font-weight:600">Welcome To</div>
<h2 class="section-title display" style="left:622px;top:672px">Lumen <span class="accent">Path</span></h2>
<div class="abs copy" style="left:622px;top:738px;width:425px"><p>Lorem Ipsum is simply dummy text of the printing and typesetting industry. Lorem Ipsum has been the industry's standard dummy text ever since the 1500s, when an unknown printer took a galley of type and scrambled it to make a type specimen book. It has survived not only five centuries, but also the leap into electronic typesetting, remaining essentially unchanged.</p></div>
<div class="btn" style="left:622px;top:897px;width:111px">Learn More</div>

<!-- programs -->
<h2 class="section-title display" style="left:0;width:1200px;text-align:center;top:1034px">Our <span class="accent">Programs</span></h2>

<article class="card" style="left:141px">
  <div class="photo" role="img" aria-label="Video still of a large audience in a lecture hall" style="background:linear-gradient(160deg,#3a2a22,#7a5a3e 50%,#b58a5e)"></div>
  <h3>Foundations 101</h3>
  <p>It is a long established fact that a reader will be distracted by the readable content of a page when looking at its layout.</p>
</article>
<article class="card" style="left:453px">
  <div class="photo" role="img" aria-label="Video still of a seated audience facing a presenter in a bright room" style="background:linear-gradient(170deg,#d9dde0,#8e8c8a 55%,#3c3a3a)"></div>
  <h3>Career Catalyst</h3>
  <p>The point of using Lorem Ipsum is that it has a more-or-less normal distribution of letters, as opposed to using 'Content here.</p>
</article>
<article class="card" style="left:765px">
  <div class="photo" role="img" aria-label="Video still of a speaker in a suit addressing a conference audience" style="background:linear-gradient(120deg,#1f3550,#5d6f82 45%,#c8a08a)"></div>
  <h3>Executive Edge</h3>
  <p>There are many variations of passages of Lorem Ipsum available, but the majority have suffered alteration in some form.</p>
</article>

<svg class="play" style="left:258px;top:1195px" viewBox="0 0 60 60"><circle cx="30" cy="30" r="27" fill="none" stroke="#fff" stroke-width="3"/><path d="M24 19 L42 30 L24 41 Z" fill="#fff"/></svg>
<svg class="play" style="left:570px;top:1195px" viewBox="0 0 60 60"><circle cx="30" cy="30" r="27" fill="none" stroke="#fff" stroke-width="3"/><path d="M24 19 L42 30 L24 41 Z" fill="#fff"/></svg>
<svg class="play" style="left:882px;top:1195px" viewBox="0 0 60 60"><circle cx="30" cy="30" r="27" fill="none" stroke="#fff" stroke-width="3"/><path d="M24 19 L42 30 L24 41 Z" fill="#fff"/></svg>

<div class="btn" style="left:545px;top:1493px;width:110px">Learn More</div>

<!-- testimonial -->
<section class="testimonial">
  <h2 class="section-title display" style="left:141px;top:86px">What Our <span class="accent">Client Say</span></h2>
  <div class="abs copy" style="left:141px;top:155px;width:455px"><p>Contrary to popular belief, Lorem Ipsum is not simply random text. It has roots in a piece of classical Latin literature from 45 BC, making it over 2000 years old. Edwin Marlow, a Latin professor at Larkfield College in Virginia, looked up one of the more obscure Latin words.</p></div>
  <div class="abs" style="left:141px;top:263px;font-size:16px;font-weight:600">Darren Holloway</div>
  <div class="btn" style="left:141px;top:309px;width:110px">Read More</div>
  <svg class="abs" style="left:550px;top:318px" width="30" height="30" viewBox="0 0 30 30"><circle cx="15" cy="15" r="13" fill="none" stroke="var(--teal)" stroke-width="1.5"/><path d="M17 10 L12 15 L17 20" fill="none" stroke="var(--teal)" stroke-width="1.8"/></svg>
  <svg class="abs" style="left:596px;top:318px" width="30" height="30" viewBox="0 0 30 30"><circle cx="15" cy="15" r="14" fill="var(--teal)"/><path d="M13 10 L18 15 L13 20" fill="none" stroke="#fff" stroke-width="1.8"/></svg>
  <div class="photo" role="img" aria-label="Video still of a coaching session between two women in a bright room with a yellow armchair and a sofa" style="left:650px;top:49px;width:409px;height:312px;background:linear-gradient(100deg,#e9e8e6,#d8d4cd 45%,#c7a98b 75%,#b48a63)"></div>
  <svg class="play" style="left:824px;top:175px" viewBox="0 0 60 60"><circle cx="30" cy="30" r="27" fill="none" stroke="#fff" stroke-width="3"/><path d="M24 19 L42 30 L24 41 Z" fill="#fff"/></svg>
</section>

<!-- about -->
<div class="frame-red" style="left:141px;top:2109px;width:321px;height:351px"></div>
<div class="photo" role="img" aria-label="Photo of a smiling coach holding a folder beside a flip chart while an audience listens" style="left:159px;top:2127px;width:377px;height:405px;background:linear-gradient(150deg,#e9e6e1,#c9c2b8 50%,#3a302a)"></div>
<div class="frame-teal" style="left:421px;top:2430px;width:131px;height:119px"></div>
<h2 class="section-title display" style="left:617px;top:2139px">About <span class="accent">Us</span></h2>
<div class="abs copy" style="left:617px;top:2203px;width:445px">
  <p>Lorem Ipsum is simply dummy text of the printing and typesetting industry. Lorem Ipsum has been the industry's standard dummy text ever since the 1500s, when an unknown printer took a galley of type and scrambled it to make a type specimen book. It has survived not only five centuries, but also the leap into electronic typesetting, remaining essentially unchanged.</p>
  <p style="margin-top:13px">There are many variations of passages of Lorem Ipsum available, but the majority have suffered alteration in some form, by injected humour, or randomised words which don't look even slightly believable. If you are going to use a passage of Lorem Ipsum, you need to be sure there isn't anything embarrassing hidden in the middle of text</p>
</div>
<div class="btn" style="left:617px;top:2491px;width:111px">Learn More</div>

<!-- footer -->
<footer class="site-footer" role="img" aria-label="Dimmed photo of a group seated in a workshop">
  <div class="footer-brand">LUMEN PATH</div>
  <svg class="abs" style="left:530px;top:151px" width="140" height="22" viewBox="0 0 140 22" aria-label="Social links">
    <circle cx="10" cy="11" r="8" fill="none" stroke="#fff" stroke-width="2"/>
    <circle cx="51" cy="11" r="8" fill="none" stroke="#fff" stroke-width="2"/>
    <circle cx="92" cy="11" r="8" fill="none" stroke="#fff" stroke-width="2"/>
    <circle cx="130" cy="11" r="8" fill="none" stroke="#fff" stroke-width="2"/>
  </svg>
  <div class="contact" style="left:308px">
    <svg width="16" height="20" viewBox="0 0 16 20" style="margin-top:3px"><path d="M8 1a6 6 0 0 0-6 6c0 4.5 6 11 6 11s6-6.5 6-11a6 6 0 0 0-6-6z" fill="none" stroke="var(--coral)" stroke-width="2"/><circle cx="8" cy="7" r="2" fill="var(--coral)"/></svg>
    <span style="width:180px">Address Line 1, Address Line 2, Address Line 3.</span>
  </div>
  <div class="contact" style="left:559px">
    <svg width="18" height="14" viewBox="0 0 18 14" style="margin-top:5px"><rect x="0" y="0" width="18" height="14" rx="2" fill="var(--coral)"/><path d="M1 1 L9 8 L17 1" fill="none" stroke="#2e2724" stroke-width="1.5"/></svg>
    <span>info@lumenpath.com</span>
  </div>
  <div class="contact" style="left:769px">
    <svg width="17" height="17" viewBox="0 0 24 24" style="margin-top:3px"><path d="M6.6 10.8a15.1 15.1 0 0 0 6.6 6.6l2.2-2.2a1 1 0 0 1 1-.25 11.4 11.4 0 0 0 3.6.57 1 1 0 0 1 1 1V20a1 1 0 0 1-1 1A17 17 0 0 1 3 4a1 1 0 0 1 1-1h3.5a1 1 0 0 1 1 1c0 1.25.2 2.45.57 3.6a1 1 0 0 1-.25 1z" fill="var(--coral)"/></svg>
    <span>123-456-7890</span>
  </div>
  <div class="rule"></div>
  <div class="legal" style="left:141px">© Lumen Path 2024. All rights reserved.</div>
  <div class="legal" style="right:141px">Privacy Policy &nbsp;|&nbsp; Terms of Service</div>
</footer>

</body>
</html>
```